Wordpress Design Project

I now need a Wordpress theme for my new business.
The business offers consultancy on Information Management, Knowledge Management, Records Management and Document Management.
The winning designer must be able to set up the site for me on my webspace provided by Tallowbrook Hosting, or talk me through how to do this.
I already have a logo designed which you can see by viewing my profile on here. I am happy to send copies of the original artwork to bidders.
I recently sold my interest in a very similar business, and want a website similar to (but not the same as) the previous company (who are now my competition!) This website can be viewed at www.qardvane.com
Categories will be similar, but I would like everything to be as configurable as possible.
I have a strong preference for clean unfussy design.
I want original design please. Please no templates from free to use sites with stock images... no jigsaw pictures!!!!
Love this one... http://www.felquist.tv/
Please get in touch with any questions.
Updates
Project Deadline Extended
Reason: All of these are too generic (brief says no jigsaw puzzle images), or have copied QDV which is the COMPETITION - so I don't want the site to look like theirs
Project Deadline Extended
Reason: Please keep trying people
Business
Business

```html
<!DOCTYPE html>
<html lang="en">
<head>
<meta charset="utf-8">
<title>Brenlow Professional Services</title>
<link href="https://fonts.googleapis.com/css2?family=Source+Sans+3:wght@400;600;700&display=swap" rel="stylesheet">
<style>
:root{
  --navy:#163e7c;
  --blue:#1f5aa3;
  --btn-top:#3d95d8;
  --btn-bottom:#1766ae;
  --text:#2b2b2b;
  --frame:#b9d3ea;
  --footer-top:#2f82c2;
  --footer-bottom:#123a72;
  --base:#0f2d57;
  --white:#ffffff;
}
*{box-sizing:border-box;margin:0;padding:0}
html,body{width:1200px;height:2228px;overflow:hidden;background:var(--white)}
body{position:relative;font-family:"Source Sans 3",Arial,sans-serif;color:var(--text)}
.abs{position:absolute}
a{text-decoration:none}

/* header */
.brand{left:30px;top:30px;display:flex;align-items:center;gap:18px}
.brand-dot{width:88px;height:88px;border-radius:50%;background:var(--blue)}
.brand-name{font-size:27px;font-weight:600;color:var(--navy);line-height:30px}
.main-nav a{position:absolute;top:78px;font-size:22px;color:var(--navy);white-space:nowrap}
.band{left:0;width:1200px;height:16px;background:linear-gradient(#3a6fb0,#0f3c7c 55%,#0a2f64);box-shadow:0 3px 5px rgba(0,0,0,.25)}

/* hero */
.hero-title{left:90px;top:268px;font-size:42px;font-weight:600;color:var(--navy)}
.hero-sub{left:90px;top:332px;font-size:34px;font-weight:600;color:var(--navy)}
.btn{display:flex;align-items:center;justify-content:center;gap:8px;color:var(--white);font-size:20px;background:linear-gradient(var(--btn-top),var(--btn-bottom));border:1px solid #0f4f8f}
.btn svg{width:11px;height:12px}
.hero-art{left:683px;top:223px;width:468px;height:319px;background:radial-gradient(ellipse at 55% 50%,#b9cfe6,#e6edf4 45%,#ffffff 72%)}

/* welcome */
.section-title{font-size:29px;font-weight:400;color:var(--navy)}
.welcome-text{left:25px;top:643px;width:800px;font-size:16px;letter-spacing:.15px;line-height:28.2px}
.welcome-text p+p{text-indent:74px}
.projects{left:851px;top:610px;width:333px;height:418px;border:1px solid var(--frame)}
.photo{border-radius:8px;border:1px solid #aac6e2;box-shadow:3px 4px 5px rgba(0,0,0,.45)}
.project-title{left:966px;top:866px;font-size:21px;font-weight:400;color:var(--navy)}
.project-text{left:876px;top:896px;width:300px;font-size:16px;line-height:28px}

/* service grid */
.card-title{font-size:20px;font-weight:400;color:var(--navy);text-align:center;width:300px}
.card-text{font-size:16px;line-height:28px;width:290px}
.card-more{font-size:16px;color:var(--text)}

/* footer */
.footer{left:0;top:1861px;width:1200px;height:310px;background:linear-gradient(var(--footer-top),var(--footer-bottom))}
.copyright{left:0;top:2171px;width:1200px;height:57px;background:var(--base);border-top:3px solid #1b4d8e;color:#e6eef8;font-size:13px;text-align:center;line-height:54px}
.f-head{font-size:16px;font-weight:400;color:#eaf3ff}
.f-list{font-size:12.5px;color:var(--white);line-height:28px;list-style:none}
.f-item{font-size:12.5px;color:var(--white);padding-left:22px;position:relative}
.f-item svg{position:absolute;left:0;top:6px;width:11px;height:16px}
.stories .f-item{line-height:28px}
.news .f-item{line-height:21px}
.news .f-item+.f-item{margin-top:22px}
.f-link{font-size:13px;color:var(--white)}
.news-input{left:891px;top:2005px;width:257px;height:39px;background:var(--white);border:1px solid #0e3a6d}
</style>
</head>
<body>

<header>
  <div class="abs brand"><span class="brand-dot"></span><span class="brand-name">Brenlow<br>Professional Services</span></div>
  <nav class="main-nav">
    <a class="abs" style="left:590px">Home</a>
    <a class="abs" style="left:665px">About Us</a>
    <a class="abs" style="left:774px">Services</a>
    <a class="abs" style="left:872px">Technology</a>
    <a class="abs" style="left:1004px">News</a>
    <a class="abs" style="left:1077px">Contact</a>
  </nav>
</header>

<div class="abs band" style="top:159px"></div>

<section class="hero">
  <h1 class="abs hero-title">Professional Services</h1>
  <h2 class="abs hero-sub">for Business Management</h2>
  <a class="abs btn" style="left:358px;top:402px;width:134px;height:33px">Read More <svg viewBox="0 0 10 12"><path d="M0 0L10 6L0 12Z" fill="#fff"/></svg></a>
  <div class="abs hero-art" role="img" aria-label="Illustration of blue figures assembling large grey puzzle pieces under the words Professional Service"></div>
</section>

<div class="abs band" style="top:566px"></div>

<section class="welcome">
  <h2 class="abs section-title" style="left:25px;top:604px">Welcome to Brenlow</h2>
  <div class="abs welcome-text">
    <p>Lorem Ipsum is simply dummy text of the printing and typesetting industry. Lorem Ipsum has been the industry's standard dummy text ever since the 1500s, when an unknown printer took a galley of type and scrambled it to make a type specimen book. It has survived not only five centuries, but also the leap into electronic typesetting, remaining essentially unchanged. It was popularised in the 1960s with the release of Fennick sheets containing Lorem Ipsum passages, and more recently with desktop publishing software like Quillmark Pages including versions of Lorem Ipsum.</p>
    <p>Lorem Ipsum is simply dummy text of the printing and typesetting industry. Lorem Ipsum has been the industry's standard dummy text ever since the 1500s, when an unknown printer took a galley of type and scrambled it to make a type specimen book. It has survived not only five centuries, but also the leap into electronic typesetting, remaining essentially unchanged. It was popularised in the 1960s with the release of Fennick sheets containing Lorem Ipsum passages, and more recently with desktop publishing software like Quillmark Pages of Lorem Ipsum.</p>
  </div>
  <a class="abs btn" style="left:674px;top:979px;width:134px;height:32px">Read More <svg viewBox="0 0 10 12"><path d="M0 0L10 6L0 12Z" fill="#fff"/></svg></a>
</section>

<aside class="abs projects"></aside>
<h2 class="abs section-title" style="left:863px;top:626px">Recent Projects</h2>
<div class="abs photo" style="left:869px;top:676px;width:301px;height:175px;background:linear-gradient(135deg,#d9dde2,#f4f5f6 45%,#6b6f78)" role="img" aria-label="Photo of a business presentation at a flip chart"></div>
<h3 class="abs project-title">Project Title</h3>
<p class="abs project-text">Lorem Ipsum has been the industry's stand-ard dummy text ever since the 1500s</p>
<a class="abs btn" style="left:1029px;top:964px;width:134px;height:31px">Read More <svg viewBox="0 0 10 12"><path d="M0 0L10 6L0 12Z" fill="#fff"/></svg></a>

<section class="services">
  <div class="abs photo" style="left:40px;top:1072px;width:303px;height:175px;background:linear-gradient(135deg,#e9f0f7,#7fa6cf 50%,#e9eef5)" role="img" aria-label="Business people standing on puzzle pieces"></div>
  <div class="abs photo" style="left:457px;top:1072px;width:303px;height:175px;background:radial-gradient(circle,#efe8cf 18%,#f3f6f9 40%,#ffffff)" role="img" aria-label="Diagram of a collaborative database linked to business functions"></div>
  <div class="abs photo" style="left:861px;top:1072px;width:302px;height:175px;background:linear-gradient(#ffffff,#ececec)" role="img" aria-label="Hand written business words with success marked in red"></div>

  <h3 class="abs card-title" style="left:26px;top:1264px">Information Management</h3>
  <h3 class="abs card-title" style="left:446px;top:1264px">Knowledge Management</h3>
  <h3 class="abs card-title" style="left:854px;top:1264px">Records Management</h3>

  <p class="abs card-text" style="left:43px;top:1302px">We help you map, classify and govern the information your business relies on, so the right people can find it fast</p>
  <p class="abs card-text" style="left:463px;top:1302px">Capture the expertise held by your people and turn it into shared know-how through practical processes and tools</p>
  <p class="abs card-text" style="left:869px;top:1302px">Retention schedules, file plans and audit-ready policies that keep your records compliant, secure and easy to find</p>

  <a class="abs card-more" style="left:245px;top:1416px">Read More&gt;&gt;</a>
  <a class="abs card-more" style="left:665px;top:1416px">Read More&gt;&gt;</a>
  <a class="abs card-more" style="left:1071px;top:1416px">Read More&gt;&gt;</a>

  <div class="abs photo" style="left:40px;top:1463px;width:303px;height:176px;background:linear-gradient(#ffffff,#8a9fb8 60%,#1c2230)" role="img" aria-label="Silhouettes of business people in front of a globe"></div>
  <div class="abs photo" style="left:457px;top:1463px;width:303px;height:176px;background:radial-gradient(ellipse,#5b7698 35%,#2b4f82 55%,#ffffff 72%)" role="img" aria-label="Circular chart of business process solutions"></div>
  <div class="abs photo" style="left:861px;top:1463px;width:302px;height:176px;background:linear-gradient(90deg,#d8352a,#f08a1e 35%,#e4d21c 60%,#3fb33a)" role="img" aria-label="Rising bar chart with an arrow"></div>

  <h3 class="abs card-title" style="left:31px;top:1656px">Document Management</h3>
  <h3 class="abs card-title" style="left:454px;top:1656px">Governance &amp; Compliance</h3>
  <h3 class="abs card-title" style="left:857px;top:1656px">Training &amp; Support</h3>

  <p class="abs card-text" style="left:43px;top:1694px">Selection and rollout of document systems with version control, workflow and search your teams will really use</p>
  <p class="abs card-text" style="left:467px;top:1694px">Policies and reviews aligned to data protection and information duties, with clear ownership across your organisation</p>
  <p class="abs card-text" style="left:871px;top:1694px">Hands-on workshops and ongoing guidance that give staff confidence to manage information well after go-live</p>

  <a class="abs card-more" style="left:245px;top:1809px">Read More&gt;&gt;</a>
  <a class="abs card-more" style="left:669px;top:1809px">Read More&gt;&gt;</a>
  <a class="abs card-more" style="left:1073px;top:1809px">Read More&gt;&gt;</a>
</section>

<footer>
  <div class="abs footer"></div>

  <h4 class="abs f-head" style="left:46px;top:1884px">Quick Links</h4>
  <ul class="abs f-list" style="left:46px;top:1916px">
    <li>Home</li><li>Services</li><li>Technology</li><li>News</li><li>Contact</li>
  </ul>

  <h4 class="abs f-head" style="left:208px;top:1882px">Brenlow Success Stories</h4>
  <div class="abs stories" style="left:204px;top:1915px;width:244px">
    <p class="f-item"><svg viewBox="0 0 11 16"><path d="M0 0L11 8L0 16Z" fill="#fff"/></svg>There are many variations of passages of Lorem Ipsum available, but the majority have suffered alteration in some form.</p>
    <p class="f-item" style="margin-top:10px"><svg viewBox="0 0 11 16"><path d="M0 0L11 8L0 16Z" fill="#fff"/></svg>There are many variations of passages of Lorem Ipsum available, but the majority have suffered alteration in some form</p>
  </div>
  <a class="abs f-link" style="left:375px;top:2100px">View All &gt;&gt;</a>

  <h4 class="abs f-head" style="left:526px;top:1885px">News &amp;Blogs</h4>
  <div class="abs news" style="left:518px;top:1922px;width:262px">
    <p class="f-item"><svg viewBox="0 0 11 16"><path d="M0 0L11 8L0 16Z" fill="#fff"/></svg>This book is a treatise on the theory of ethics, very popular during the Renaissance.</p>
    <p class="f-item"><svg viewBox="0 0 11 16"><path d="M0 0L11 8L0 16Z" fill="#fff"/></svg>This book is a treatise on the theory of ethics, very popular during the Renaissance.</p>
    <p class="f-item"><svg viewBox="0 0 11 16"><path d="M0 0L11 8L0 16Z" fill="#fff"/></svg>This book is a treatise on the theory of ethics, very popular during the Renaissance.</p>
  </div>
  <a class="abs f-link" style="left:717px;top:2099px">View All &gt;&gt;</a>

  <h4 class="abs f-head" style="left:890px;top:1885px">Newsletter Signup</h4>
  <p class="abs f-list" style="left:890px;top:1918px;width:240px">Sign up and we'll keep you notified on any announcements regarding changes to our site or our products &amp; services</p>
  <div class="abs news-input"></div>
  <a class="abs f-link" style="left:1075px;top:2060px;font-size:16px;display:flex;align-items:center;gap:10px">Sign up <svg width="11" height="16" viewBox="0 0 11 16"><path d="M0 0L11 8L0 16Z" fill="#fff"/></svg></a>

  <div class="abs copyright">© Brenlow.com2012. All Rights Reserved .</div>
</footer>

</body>
</html>
```